" O nome Valtessora significa dentro do movimento. A clínica tem como carro chefe um trabalho chamado de videoanálise de movimento. Usamos um software para realizar análise de marcha, corrida, salto, estabilidade, flexibilidade entre outros. Identificamos alteraçoes no movimento que possam ser a causa de dor ou diminmuiçao no rendimento físico-funcional. Alteraçoes identificadas entramos com a reabilitaçao usando Pilates, RPG, Hidroterapia, Treinamento Funcional, Osteopatia entre outros. Nosso foco: resultados! "

```html
<!DOCTYPE html>
<html lang="pt-BR">
<head>
<meta charset="utf-8">
<title>Valtessora — Pasta e Envelope</title>
<link href="https://fonts.googleapis.com/css2?family=Exo+2:wght@400;600;700&display=swap" rel="stylesheet">
<style>
  :root {
    --bg: #eef0f2;
    --paper: #ffffff;
    --brand-blue: #1f57a8;
    --flap-blue: #4a86c8;
    --mark-blue: #3d7bd0;
    --accent-blue: #2f6fc6;
    --accent-grey: #9a9ea4;
    --ink-grey: #6b7076;
    --tagline-blue: #5b8fd0;
    --edge: #d9dde1;
  }
  * { margin: 0; padding: 0; box-sizing: border-box; }
  html, body { width: 1200px; height: 1200px; overflow: hidden; }
  body {
    background: var(--bg);
    font-family: "Exo 2", sans-serif;
    position: relative;
  }
  .envelope {
    position: absolute;
    left: 509px; top: 247px;
    width: 607px; height: 838px;
    background: var(--paper);
    border: 1px solid var(--edge);
    overflow: hidden;
  }
  .envelope-flap { position: absolute; left: 0; top: 0; width: 100%; height: 100px; }
  .envelope-brand {
    position: absolute; left: 0; right: 0; top: 610px;
    text-align: center;
  }
  .envelope-contact {
    position: absolute; left: 0; right: 0; top: 722px;
    text-align: center; color: var(--ink-grey);
    font-size: 10px; line-height: 17px; letter-spacing: 0.2px;
  }
  .envelope-contact .web { letter-spacing: 5px; margin-top: 2px; }
  .folder {
    position: absolute;
    left: 108px; top: 96px;
    width: 607px; height: 816px;
    background: var(--paper);
    border: 1px solid var(--edge);
    overflow: hidden;
  }
  .folder-brand {
    position: absolute; left: 0; right: 0; top: 42px;
    text-align: center;
  }
  .brand-dot {
    display: block; margin: 0 auto 12px;
    width: 40px; height: 40px; border-radius: 50%;
    background: var(--mark-blue);
  }
  .brand-name {
    display: block; font-weight: 700; color: var(--brand-blue);
    font-size: 46px; line-height: 1; letter-spacing: -0.5px;
  }
  .brand-tagline {
    display: block; margin-top: 3px;
    font-size: 11px; color: var(--tagline-blue); letter-spacing: 0.6px;
  }
  .envelope-brand .brand-dot { width: 34px; height: 34px; margin-bottom: 10px; }
  .envelope-brand .brand-name { font-size: 36px; }
  .envelope-brand .brand-tagline { font-size: 9px; }
  .folder-accent { position: absolute; left: 0; top: 262px; width: 470px; height: 412px; }
</style>
</head>
<body>
  <section class="envelope">
    <svg class="envelope-flap" viewBox="0 0 607 100" preserveAspectRatio="none" aria-hidden="true">
      <polygon points="0,0 607,0 582,100 0,100" fill="var(--flap-blue)"/>
    </svg>
    <div class="envelope-brand">
      <span class="brand-dot"></span>
      <span class="brand-name">Valtessora</span>
      <span class="brand-tagline">Clínica da Performance Humana</span>
    </div>
    <div class="envelope-contact">
      <p>Endereço: Rua Exemplo, 999 Cep: 99999-00 - Bairro - XX</p>
      <p>Fone: (00) 0000-0000 contato@valtessora.com.br</p>
      <p class="web">www.valtessora.com.br</p>
    </div>
  </section>

  <section class="folder">
    <div class="folder-brand">
      <span class="brand-dot"></span>
      <span class="brand-name">Valtessora</span>
      <span class="brand-tagline">Clínica da Performance Humana</span>
    </div>
    <svg class="folder-accent" viewBox="0 0 470 412" role="img" aria-label="Grande elemento decorativo da marca em azul e cinza, sangrando pela borda esquerda">
      <defs>
        <linearGradient id="accentFill" x1="0" y1="0" x2="1" y2="1">
          <stop offset="0" stop-color="var(--accent-blue)"/>
          <stop offset="0.45" stop-color="#7d9cc6"/>
          <stop offset="1" stop-color="var(--accent-grey)"/>
        </linearGradient>
      </defs>
      <ellipse cx="150" cy="206" rx="318" ry="206" fill="url(#accentFill)"/>
    </svg>
  </section>
</body>
</html>
```